Brookmere Osteopathy flyer

I want a clean clear DL flyer (but also want an A4 poster) promoting a new Osteopathic business in a semi rural area in Tasmania (Australia).
It can have pictures like the examples attached to show people what Osteopathy is (its like Chiropractic and physiotherapy).
I am the sole practioner and am male, so any pictures would be best to be a white male if possible.
I've attached some wording, you can use all, or none of it
I don't have a phone number for the business yet
info@brookmereosteopathy.example
www.brookmereosteopathy.example
Target Market(s)
Australians, from tradies, professionals, babies to retired people
Industry/Entity Type
Health
Look and feel

```html
<!DOCTYPE html>
<html lang="en">
<head>
<meta charset="utf-8">
<title>Brookmere Osteopathy Flyer</title>
<link rel="stylesheet" href="https://fonts.googleapis.com/css2?family=League+Spartan:wght@600;700;800&family=Questrial&family=Montserrat:wght@500&display=swap">
<style>
  :root {
    --cream: #fdf5f1;
    --blue: #1f98d4;
    --orange: #f0974a;
    --ink: #1d1d1f;
    --skin-light: #f3ddd0;
    --skin-mid: #d9b39c;
    --cloth-grey: #8c8f94;
  }
  * { margin: 0; padding: 0; box-sizing: border-box; }
  html, body { width: 897px; height: 1200px; overflow: hidden; background: var(--cream); }
  .flyer {
    position: relative;
    width: 897px;
    height: 1200px;
    background: var(--cream);
    font-family: "Questrial", "Century Gothic", sans-serif;
    color: var(--ink);
    overflow: hidden;
  }
  .hero-photo, .bottom-photo { position: absolute; left: 0; top: 0; }
  .brand-mark {
    position: absolute;
    left: 62px; top: 26px;
    width: 172px; height: 172px;
    display: flex; flex-direction: column; align-items: center; justify-content: center;
    gap: 10px;
  }
  .brand-mark .dot {
    width: 34px; height: 34px; border-radius: 50%;
    border: 3px solid var(--blue);
  }
  .brand-mark .brand-name {
    font-family: "League Spartan", sans-serif;
    font-weight: 600;
    font-size: 17px;
    letter-spacing: 1.5px;
    color: var(--blue);
    text-transform: uppercase;
    text-align: center;
    line-height: 1.2;
  }
  .headline {
    position: absolute;
    left: 54px; top: 222px;
    font-family: "League Spartan", sans-serif;
    font-weight: 800;
    font-size: 92px;
    line-height: 78px;
    letter-spacing: 0.5px;
  }
  .headline .line-one { display: block; color: var(--blue); }
  .headline .line-two { display: block; color: var(--orange); }
  .reasons-title {
    position: absolute;
    left: 55px; top: 416px;
    font-family: "League Spartan", sans-serif;
    font-weight: 700;
    font-size: 29px;
    line-height: 30px;
    letter-spacing: -0.2px;
  }
  .reasons-title .blue { display: block; color: var(--blue); }
  .reasons-title .orange { display: block; color: var(--orange); }
  .reasons-list {
    position: absolute;
    left: 64px; top: 521px;
    list-style: none;
    font-size: 21px;
    line-height: 27px;
  }
  .reasons-list li { display: flex; align-items: center; gap: 6px; }
  .reasons-list svg { flex: none; width: 16px; height: 16px; }
  .about-text {
    position: absolute;
    left: 65px; top: 802px;
    width: 476px;
    font-size: 16.5px;
    line-height: 23.5px;
    text-align: justify;
  }
  .contact-list {
    position: absolute;
    left: 66px; top: 971px;
    list-style: none;
    font-family: "Montserrat", sans-serif;
    font-weight: 500;
    font-size: 14px;
    line-height: 20.5px;
  }
  .contact-list li { display: flex; align-items: center; gap: 8px; }
  .contact-list svg { width: 12px; height: 12px; flex: none; }
  .call-to-action {
    position: absolute;
    left: 54px; top: 1040px;
    font-family: "League Spartan", sans-serif;
    font-weight: 700;
    font-size: 46px;
    line-height: 42px;
    letter-spacing: -0.5px;
  }
  .call-to-action .prompt { display: block; color: var(--orange); }
  .call-to-action .phone { display: block; color: var(--blue); }
  .treatment-circle {
    position: absolute;
    width: 226px; height: 226px;
    border-radius: 50%;
    border: 10px solid var(--orange);
  }
  .treatment-circle.upper { left: 607px; top: 390px; background: linear-gradient(160deg, #eef0f2 0%, #d9c2b4 55%, #f4f4f4 100%); }
  .treatment-circle.lower { left: 607px; top: 580px; background: linear-gradient(150deg, #e6e8ea 0%, #c9a994 50%, #5d6166 100%); }
</style>
</head>
<body>
<main class="flyer">
  <svg class="hero-photo" width="897" height="1200" viewBox="0 0 897 1200">
    <defs>
      <linearGradient id="heroTone" x1="0" y1="0" x2="1" y2="1">
        <stop offset="0" stop-color="#f4f2f1"/>
        <stop offset="0.5" stop-color="#e6c7b4"/>
        <stop offset="1" stop-color="#d4a88f"/>
      </linearGradient>
      <linearGradient id="bottomTone" x1="0" y1="0" x2="1" y2="1">
        <stop offset="0" stop-color="#8fa3b8"/>
        <stop offset="0.45" stop-color="#e3bfa8"/>
        <stop offset="1" stop-color="#6f7378"/>
      </linearGradient>
    </defs>
    <path role="img" aria-label="Photo: practitioner massaging a patient's shoulder"
          d="M384,0 C400,70 440,100 510,120 C620,150 680,200 700,290 C720,370 800,405 897,418 V0 Z"
          fill="url(#heroTone)"/>
    <path d="M384,0 C400,70 440,100 510,120 C620,150 680,200 700,290 C720,370 800,405 897,418"
          fill="none" stroke="var(--orange)" stroke-width="6"/>
    <path role="img" aria-label="Photo: osteopath treating the back of a man lying on a table"
          d="M335,1200 V1070 C360,1010 420,985 480,995 C530,965 570,930 605,895 C650,850 690,800 760,790 L897,798 V1200 Z"
          fill="url(#bottomTone)"/>
  </svg>

  <div class="brand-mark">
    <span class="dot"></span>
    <span class="brand-name">Brookmere<br>Osteopathy</span>
  </div>

  <h1 class="headline">
    <span class="line-one">BROOKMERE</span>
    <span class="line-two">OSTEOPATHY</span>
  </h1>

  <h2 class="reasons-title">
    <span class="blue">COMMON REASONS</span>
    <span class="orange">PEOPLE VISIT AN OSTEOPATH</span>
  </h2>

  <div class="treatment-circle upper" role="img" aria-label="Photo: practitioner assessing a woman's upper back"></div>
  <div class="treatment-circle lower" role="img" aria-label="Photo: practitioner treating a man's neck on a table"></div>

  <ul class="reasons-list">
    <li><svg viewBox="0 0 16 16"><circle cx="8" cy="8" r="6.5" fill="none" stroke="var(--orange)" stroke-width="1.6"/><path d="M4.8 8.2 L7.3 10.6 L14 3.5" fill="none" stroke="var(--orange)" stroke-width="1.8"/></svg>Sciatica</li>
    <li><svg viewBox="0 0 16 16"><circle cx="8" cy="8" r="6.5" fill="none" stroke="var(--orange)" stroke-width="1.6"/><path d="M4.8 8.2 L7.3 10.6 L14 3.5" fill="none" stroke="var(--orange)" stroke-width="1.8"/></svg>Plantar fasciitis</li>
    <li><svg viewBox="0 0 16 16"><circle cx="8" cy="8" r="6.5" fill="none" stroke="var(--orange)" stroke-width="1.6"/><path d="M4.8 8.2 L7.3 10.6 L14 3.5" fill="none" stroke="var(--orange)" stroke-width="1.8"/></svg>Tendonitis / Bursitis</li>
    <li><svg viewBox="0 0 16 16"><circle cx="8" cy="8" r="6.5" fill="none" stroke="var(--orange)" stroke-width="1.6"/><path d="M4.8 8.2 L7.3 10.6 L14 3.5" fill="none" stroke="var(--orange)" stroke-width="1.8"/></svg>Adhesive capsulitis (frozen shoulder)</li>
    <li><svg viewBox="0 0 16 16"><circle cx="8" cy="8" r="6.5" fill="none" stroke="var(--orange)" stroke-width="1.6"/><path d="M4.8 8.2 L7.3 10.6 L14 3.5" fill="none" stroke="var(--orange)" stroke-width="1.8"/></svg>Tennis / Golfers elbow</li>
    <li><svg viewBox="0 0 16 16"><circle cx="8" cy="8" r="6.5" fill="none" stroke="var(--orange)" stroke-width="1.6"/><path d="M4.8 8.2 L7.3 10.6 L14 3.5" fill="none" stroke="var(--orange)" stroke-width="1.8"/></svg>Back / neck pain</li>
    <li><svg viewBox="0 0 16 16"><circle cx="8" cy="8" r="6.5" fill="none" stroke="var(--orange)" stroke-width="1.6"/><path d="M4.8 8.2 L7.3 10.6 L14 3.5" fill="none" stroke="var(--orange)" stroke-width="1.8"/></svg>Headaches / migraines</li>
    <li><svg viewBox="0 0 16 16"><circle cx="8" cy="8" r="6.5" fill="none" stroke="var(--orange)" stroke-width="1.6"/><path d="M4.8 8.2 L7.3 10.6 L14 3.5" fill="none" stroke="var(--orange)" stroke-width="1.8"/></svg>Joint and muscle pain</li>
    <li><svg viewBox="0 0 16 16"><circle cx="8" cy="8" r="6.5" fill="none" stroke="var(--orange)" stroke-width="1.6"/><path d="M4.8 8.2 L7.3 10.6 L14 3.5" fill="none" stroke="var(--orange)" stroke-width="1.8"/></svg>Pregnancy-related discomfort</li>
    <li><svg viewBox="0 0 16 16"><circle cx="8" cy="8" r="6.5" fill="none" stroke="var(--orange)" stroke-width="1.6"/><path d="M4.8 8.2 L7.3 10.6 L14 3.5" fill="none" stroke="var(--orange)" stroke-width="1.8"/></svg>Disc related issues</li>
  </ul>

  <p class="about-text">Osteopaths use a combination of joint manipulation, targeted deep tissue massage and stretching to improve function, relieve pain and support the body’s ability to heal itself.</p>

  <ul class="contact-list">
    <li><svg viewBox="0 0 12 12"><path d="M6 11 C3 7.5 2 6 2 4.5 A4 4 0 0 1 10 4.5 C10 6 9 7.5 6 11 Z" fill="none" stroke="var(--orange)" stroke-width="1"/><circle cx="6" cy="4.5" r="1.4" fill="none" stroke="var(--orange)" stroke-width="1"/></svg>24 Mill Creek road, Brookmere</li>
    <li><svg viewBox="0 0 12 12"><circle cx="6" cy="6" r="5" fill="none" stroke="var(--orange)" stroke-width="1"/><ellipse cx="6" cy="6" rx="2.2" ry="5" fill="none" stroke="var(--orange)" stroke-width="1"/><path d="M1 6 H11" stroke="var(--orange)" stroke-width="1"/></svg>www.brookmereosteopathy.example</li>
    <li><svg viewBox="0 0 12 12"><rect x="1" y="2.5" width="10" height="7" fill="none" stroke="var(--orange)" stroke-width="1"/><path d="M1 2.5 L6 6.5 L11 2.5" fill="none" stroke="var(--orange)" stroke-width="1"/></svg>info@brookmereosteopathy.example</li>
  </ul>

  <div class="call-to-action">
    <span class="prompt">CALL US NOW!</span>
    <span class="phone">03-5550-0142</span>
  </div>
</main>
</body>
</html>
```